Special offers flyer for IT firm

We need a flyer design for our IT technical services firm based in Melbourne, Australia. We want to advertise two offerings on a double sided flyer.
-
First Offering:
Free computer system health report and audit
- health check of servers, workstations and network
- comprehensive non-technical report including recommendations
-
Second Offering:
Discounted technical support - $80* per hour
- day to day helpdesk support
- system upgrades and migrations
- cloud services design, implementation and support
- web hosting, domain names and email filtering

*exclusive of GST (must denote somewhere in small print)
-
The contact details for the offer must include room for Phone, Email and Web Address.

I am not set on the text, or any particular format, additional images would be good to break up the pages.

Target Market(s)

Professional Services small business owners (under 30 staff)

Industry/Entity Type

Computer

Requirements
Must have
• DL Sized document (210mmx99mm) portrait or landscape, double sided.

```html
<!DOCTYPE html>
<html lang="en">
<head>
<meta charset="utf-8">
<title>TenByte IT – Special Offers Flyer</title>
<link href="https://fonts.googleapis.com/css2?family=Questrial&display=swap" rel="stylesheet">
<style>
  :root {
    --brand-blue: #1f63a6;
    --brand-blue-dark: #174d84;
    --navy: #16335c;
    --label-grey: rgba(128,130,134,0.88);
    --text-dark: #2a2a2a;
    --paper: #ffffff;
    --backdrop: #2e2724;
  }
  * { box-sizing: border-box; margin: 0; padding: 0; }
  html, body {
    width: 1200px; height: 848px; overflow: hidden;
    background: var(--backdrop);
    font-family: "Questrial", "Century Gothic", sans-serif;
  }
  .sheet-pair {
    position: absolute; left: 266px; top: 89px;
    display: flex; gap: 40px;
  }
  .flyer {
    position: relative; width: 314px; height: 670px;
    background: var(--paper); overflow: hidden;
  }
  .brand {
    position: absolute; top: 0; left: 0; right: 0; height: 89px;
    display: flex; align-items: center; justify-content: center; gap: 9px;
  }
  .brand-dot { width: 14px; height: 14px; border-radius: 50%; background: var(--brand-blue); }
  .brand-name { font-size: 31px; color: var(--navy); letter-spacing: 0.5px; }
  .top-band {
    position: absolute; top: 89px; left: 0; right: 0; height: 11px;
    background: var(--brand-blue);
  }
  .photo {
    position: absolute; left: 0; right: 0; top: 107px;
  }
  .photo-keyboard {
    height: 328px;
    background: linear-gradient(160deg, #c9d0d8 0%, #7b8794 45%, #3b4450 100%);
  }
  .photo-technician {
    height: 303px;
    background: linear-gradient(150deg, #f1f1ef 0%, #d8d8d4 50%, #a7a59c 100%);
  }
  .service-label {
    position: absolute; top: 111px; left: 33px; width: 249px; height: 53px;
    background: var(--label-grey); border-radius: 0 0 8px 8px;
    color: #fff; font-size: 21px; line-height: 24px; text-align: center;
    padding-top: 3px;
  }
  .gst-badge {
    position: absolute; left: 211px; top: 306px; width: 86px; height: 86px;
    border-radius: 50%; background: radial-gradient(circle at 40% 35%, #3a8ad6, var(--brand-blue-dark));
    border: 3px solid #fff; box-shadow: 0 2px 5px rgba(0,0,0,0.35);
    color: #fff; font-size: 15px; line-height: 16px; font-weight: 700;
    display: flex; align-items: center; justify-content: center; text-align: center;
  }
  .offer-tab {
    position: absolute; left: 31px; width: 251px; height: 42px;
    background: var(--brand-blue); border-radius: 0 0 10px 10px;
    color: #fff; font-size: 23px; text-align: center; line-height: 42px;
  }
  .offer-tab.first { top: 435px; }
  .offer-tab.second { top: 410px; }
  .offer-list {
    position: absolute; left: 0; right: 12px; list-style: none;
    color: var(--text-dark); font-size: 12.5px; line-height: 14px;
  }
  .offer-list.first { top: 540px; }
  .offer-list.second { top: 472px; }
  .offer-list li { position: relative; padding-left: 57px; margin-bottom: 6px; }
  .offer-list.first li { margin-bottom: 9px; }
  .offer-list li::before {
    content: ""; position: absolute; left: 0; top: 2px; width: 54px; height: 9px;
    background: var(--brand-blue); border-radius: 0 6px 6px 0;
  }
  .contact-bar {
    position: absolute; left: 0; right: 0; bottom: 0; height: 57px;
    background: var(--brand-blue); color: #fff;
  }
  .contact-phone { position: absolute; top: 8px; left: 0; right: 0; text-align: center; font-size: 17px; }
  .contact-email, .contact-web { position: absolute; bottom: 6px; font-size: 10px; }
  .contact-email { left: 10px; }
  .contact-web { right: 10px; }
</style>
</head>
<body>
  <div class="sheet-pair">
    <section class="flyer flyer-front">
      <header class="brand"><span class="brand-dot"></span><span class="brand-name">TenByte IT</span></header>
      <div class="top-band"></div>
      <div class="photo photo-keyboard" role="img" aria-label="Close-up photo of a laptop keyboard with a small screwdriver resting on the keys"></div>
      <div class="service-label">IT technical<br>services</div>
      <h2 class="offer-tab first">First Offering:</h2>
      <ul class="offer-list first">
        <li>- Free computer system health report and audit</li>
        <li>- health check of servers, workstations and network</li>
        <li>- comprehensive non-technical report including recommendations</li>
      </ul>
      <footer class="contact-bar">
        <div class="contact-phone">Phone: 3100 - 555 - 20417</div>
        <div class="contact-email">info@tenbyteit.com</div>
        <div class="contact-web">www.tenbyteit.com</div>
      </footer>
    </section>

    <section class="flyer flyer-back">
      <header class="brand"><span class="brand-dot"></span><span class="brand-name">TenByte IT</span></header>
      <div class="top-band"></div>
      <div class="photo photo-technician" role="img" aria-label="Photo of hands using a screwdriver inside an open desktop computer case"></div>
      <div class="service-label">IT technical<br>services</div>
      <div class="gst-badge">exclusive<br>of GST</div>
      <h2 class="offer-tab second">Second Offering:</h2>
      <ul class="offer-list second">
        <li>Discounted technical support - $80* per hour</li>
        <li>day to day helpdesk support</li>
        <li>system upgrades and migrations</li>
        <li>cloud services design, implementation and support</li>
        <li>web hosting, domain names and email filtering</li>
      </ul>
      <footer class="contact-bar">
        <div class="contact-phone">Phone: 3100 - 555 - 20417</div>
        <div class="contact-email">info@tenbyteit.com</div>
        <div class="contact-web">www.tenbyteit.com</div>
      </footer>
    </section>
  </div>
</body>
</html>
```